Copper Ridge Business Cards For New Startup

I am looking for you to design some business cards for a new startup https://copperridgehub.example. I have supplied logo, brand guidelines and our signatures as a guide.

We need this to reflect the brand guidelines and the website for brand consistency,

What is Copper Ridge?

Mallorca's Business Growth Community
Join your new business community full of passionate entrepreneurs who
love to solve problems and help each other grow together!

Any questions you can ask.

Target Market(s)

Business to Business

Contact Information for Business Card

These are attached (signatures) to the job

Font styles to use
Other font styles liked:
• Open Sans

Requirements
Must have
• Match design guidelines
Nice to have
• Photos of our faces so people remember us

```html
<!DOCTYPE html>
<html lang="en">
<head>
<meta charset="utf-8">
<title>Copper Ridge Business Card</title>
<link href="https://fonts.googleapis.com/css2?family=Open+Sans:wght@400;600;700&display=swap" rel="stylesheet">
<style>
  :root {
    --olive: #666600;
    --olive-dark: #5a5a00;
    --white: #ffffff;
    --paper-light: #ffffff;
    --paper-grey: #e4e4e4;
    --backdrop: #3b3b3b;
    --photo-light: #f2f2f2;
    --photo-mid: #c9ccd2;
    --photo-suit: #5d6f8c;
  }
  * { box-sizing: border-box; margin: 0; padding: 0; }
  html, body { width: 1200px; height: 1000px; overflow: hidden; }
  body {
    background: var(--backdrop);
    font-family: "Open Sans", sans-serif;
    position: relative;
  }
  .card {
    position: absolute;
    left: 250px;
    width: 700px;
    height: 400px;
    border-radius: 26px;
    overflow: hidden;
  }
  /* Back side */
  .card-back {
    top: 60px;
    background: var(--olive);
    display: flex;
    align-items: center;
    justify-content: center;
    gap: 30px;
  }
  .brand-circle {
    width: 96px;
    height: 96px;
    border: 3px solid var(--white);
    border-radius: 50%;
  }
  .card-back .brand-name {
    color: var(--white);
    font-size: 46px;
    font-weight: 600;
    letter-spacing: 1px;
  }
  /* Front side */
  .card-front {
    top: 520px;
    background: linear-gradient(160deg, var(--paper-grey) 0%, var(--paper-light) 70%);
  }
  .portrait {
    position: absolute;
    left: 30px;
    top: 30px;
    width: 400px;
    height: 370px;
    background: radial-gradient(ellipse at 55% 35%, var(--photo-mid) 0%, var(--photo-light) 55%, transparent 75%),
                linear-gradient(to bottom, transparent 55%, var(--photo-suit) 100%);
    border-radius: 6px 6px 0 0;
  }
  .name-band {
    position: absolute;
    left: 0;
    bottom: 0;
    width: 100%;
    height: 112px;
    background: var(--olive);
    clip-path: polygon(0 0, 58% 0, 66% 100%, 0 100%);
    padding: 14px 0 0 34px;
    color: var(--white);
  }
  .person-name { font-size: 25px; font-weight: 700; line-height: 1.2; }
  .person-role { font-size: 15px; font-weight: 400; margin-top: 2px; }
  .brand-block {
    position: absolute;
    right: 30px;
    top: 42px;
    width: 250px;
    display: flex;
    flex-direction: column;
    align-items: center;
  }
  .brand-block .brand-circle {
    width: 120px;
    height: 120px;
    border-color: var(--olive);
  }
  .brand-block .brand-name {
    margin-top: 12px;
    color: var(--olive);
    font-size: 30px;
    font-weight: 600;
    letter-spacing: 0.5px;
  }
  .contact-list {
    position: absolute;
    right: 30px;
    top: 238px;
    list-style: none;
    text-align: right;
    color: var(--olive);
    font-size: 16px;
    line-height: 1.45;
  }
  .contact-list li { display: flex; align-items: center; justify-content: flex-end; gap: 8px; }
  .contact-list svg { width: 14px; height: 14px; }
  .contact-list .web { font-weight: 700; }
  .social-row {
    position: absolute;
    right: 30px;
    bottom: 26px;
    display: flex;
    gap: 10px;
  }
  .social-dot {
    width: 28px;
    height: 28px;
    border-radius: 50%;
    background: var(--olive);
  }
</style>
</head>
<body>
  <section class="card card-back">
    <div class="brand-circle"></div>
    <div class="brand-name">COPPER RIDGE</div>
  </section>

  <section class="card card-front">
    <div class="portrait" role="img" aria-label="Portrait photo of Marco Ferrer"></div>
    <div class="name-band">
      <div class="person-name">Marco Ferrer</div>
      <div class="person-role">Founder &amp; Growth Hacker | Copper Ridge</div>
    </div>

    <div class="brand-block">
      <div class="brand-circle"></div>
      <div class="brand-name">COPPER RIDGE</div>
    </div>

    <ul class="contact-list">
      <li>+34 611 482 905
        <svg viewBox="0 0 24 24" fill="none" stroke="#666600" stroke-width="2.4" stroke-linecap="round" stroke-linejoin="round"><path d="M5 3h4l2 5-2.5 1.5a11 11 0 0 0 6 6L16 13l5 2v4a2 2 0 0 1-2 2A17 17 0 0 1 3 5a2 2 0 0 1 2-2z"/></svg>
      </li>
      <li>mf@copperridgehub.example
        <svg viewBox="0 0 24 24" fill="none" stroke="#666600" stroke-width="2.4" stroke-linejoin="round"><rect x="3" y="5" width="18" height="14" rx="1"/><path d="M3 6l9 7 9-7"/></svg>
      </li>
      <li><span class="web">copperridgehub.example</span>
        <svg viewBox="0 0 24 24" fill="none" stroke="#666600" stroke-width="2"><circle cx="12" cy="12" r="9"/><path d="M3 12h18M12 3c3 3 3 15 0 18M12 3c-3 3-3 15 0 18"/></svg>
      </li>
    </ul>

    <div class="social-row" aria-label="Social channels">
      <span class="social-dot"></span>
      <span class="social-dot"></span>
      <span class="social-dot"></span>
      <span class="social-dot"></span>
      <span class="social-dot"></span>
    </div>
  </section>
</body>
</html>
```